Business card

would like a double sided business card made up with my logos provided.
Prefer card to have black background and to use the black logos, with matching blue writing for the text.
One side to just be the logo, (Try to use both the black logos)
the other side to have the logo and also my credentials/business information.

Covering all aspects of Carpentry and Building Services

Marcus Tolvey
Qualified Carpenter
Mob: 0417263948
Email: rkt.joinery@mailbright.com
ABN: 47 615 209 834

Industry/Entity Type

Business

Contact Information for Business Card

Marcus Tolvey
Qualified Carpenter
Mob: 0417263948
ABN: 47 615 209 834

Requirements
Must have
• Please try to use both the black logos and incorporate into the card.

```html
<!DOCTYPE html>
<html lang="en">
<head>
<meta charset="utf-8">
<title>RKT Joinery – Business Card</title>
<link rel="stylesheet" href="https://fonts.googleapis.com/css2?family=Lato:wght@400;700&family=Montserrat:wght@600&family=Open+Sans:ital,wght@1,400&display=swap">
<style>
  :root {
    --backdrop: #8a8a8a;
    --card-black: #0b0c0e;
    --card-white: #eeeeec;
    --accent-blue: #1f9ad6;
    --text-white: #f4f4f4;
    --text-dark: #2b2b2b;
  }
  * { margin: 0; padding: 0; box-sizing: border-box; }
  html, body {
    width: 1200px; height: 955px; overflow: hidden;
    background: var(--backdrop);
  }
  .canvas { position: relative; width: 1200px; height: 955px; }
  .card {
    position: absolute; width: 560px; height: 330px;
    background: var(--card-black); overflow: hidden;
    box-shadow: 0 10px 30px rgba(0,0,0,.35);
  }
  .card svg { position: absolute; inset: 0; }
  .card--logo { left: 580px; top: 100px; }
  .card--details { left: 70px; top: 520px; }

  .brand {
    position: absolute; display: flex; align-items: center; gap: 10px;
    font-family: "Montserrat", sans-serif; font-weight: 600;
    color: var(--text-white); white-space: nowrap;
  }
  .brand__mark { background: var(--accent-blue); flex: none; }
  .card--logo .brand { left: 200px; top: 22px; font-size: 28px; letter-spacing: 1px; }
  .card--logo .brand__mark { width: 16px; height: 16px; }
  .card--details .brand { right: 30px; top: 130px; font-size: 28px; letter-spacing: 1px; }
  .card--details .brand__mark { width: 18px; height: 18px; }

  .tagline {
    position: absolute; left: 110px; bottom: 42px;
    font-family: "Open Sans", sans-serif; font-style: italic;
    font-size: 14px; color: var(--text-white); white-space: nowrap;
  }
  .person { position: absolute; left: 40px; top: 100px; font-family: "Lato", sans-serif; }
  .person__name { font-weight: 700; font-size: 16px; color: var(--text-dark); }
  .person__role { font-size: 13px; color: var(--accent-blue); }

  .contacts {
    position: absolute; left: 330px; top: 232px; list-style: none;
    font-family: "Lato", sans-serif; font-size: 15px; color: var(--accent-blue);
  }
  .contacts li { display: flex; align-items: center; gap: 8px; height: 22px; white-space: nowrap; }
  .contacts svg { position: static; width: 14px; height: 14px; flex: none; }
</style>
</head>
<body>
<main class="canvas">

  <section class="card card--logo" aria-label="Business card, logo side">
    <svg viewBox="0 0 560 330" width="560" height="330" aria-hidden="true">
      <polygon points="0,0 0,330 250,130" fill="var(--card-white)"/>
      <polyline points="0,0 250,130 0,330" fill="none" stroke="var(--accent-blue)" stroke-width="3"/>
      <polygon points="560,110 560,330 330,150" fill="var(--card-white)"/>
      <polyline points="560,110 330,150 560,330" fill="none" stroke="var(--accent-blue)" stroke-width="3"/>
    </svg>
    <div class="brand"><span class="brand__mark"></span>RKT JOINERY</div>
    <p class="tagline">Covering all aspects of Carpentry and Building Services</p>
  </section>

  <section class="card card--details" aria-label="Business card, details side">
    <svg viewBox="0 0 560 330" width="560" height="330" aria-hidden="true">
      <polygon points="0,0 0,330 300,150" fill="var(--card-white)"/>
      <polyline points="0,0 300,150 0,330" fill="none" stroke="var(--accent-blue)" stroke-width="3"/>
    </svg>
    <div class="person">
      <p class="person__name">Marcus Tolvey</p>
      <p class="person__role">Qualified Carpenter</p>
    </div>
    <div class="brand"><span class="brand__mark"></span>RKT JOINERY</div>
    <ul class="contacts">
      <li>
        <svg viewBox="0 0 14 14" aria-hidden="true"><rect x="1" y="1" width="12" height="12" fill="var(--text-white)"/><rect x="4.5" y="3" width="5" height="8" rx="1" fill="none" stroke="var(--card-black)" stroke-width="1.2"/></svg>
        0417263948
      </li>
      <li>
        <svg viewBox="0 0 14 14" aria-hidden="true"><rect x="1" y="1" width="12" height="12" fill="var(--text-white)"/><path d="M3 7 L7 3.5 L11 7 V11 H3 Z" fill="var(--card-black)"/></svg>
        ABN: 47 615 209 834
      </li>
      <li>
        <svg viewBox="0 0 14 14" aria-hidden="true"><rect x="1" y="1" width="12" height="12" fill="var(--text-white)"/><rect x="3" y="4.5" width="8" height="5.5" fill="none" stroke="var(--card-black)" stroke-width="1.2"/><path d="M3 4.5 L7 8 L11 4.5" fill="none" stroke="var(--card-black)" stroke-width="1.2"/></svg>
        rkt.joinery@mailbright.com
      </li>
    </ul>
  </section>

</main>
</body>
</html>
```